UI Improvement for FlorvaLink app

We are looking for a talented UI/UX designer to REFINE and enhance the visual design of our mobile application, FlorvaLink. The app is fully functional, but we need a designer to improve its aesthetics by specifying design elements such as fonts, colors, spacing, and component styles.
Your task will be to analyze the CURRENT UI and provide detailed design specifications that will make the app more visually appealing, modern, and user-friendly.
TODO:
Review the existing FlorvaLink app design (see attachments) and identify areas for visual improvement.
Provide a detailed UI style guide, including:
Typography (font choices, sizes, and weights)
Color palette (primary, secondary, and accent colors)
Component styling (buttons, forms, icons, and interactive elements)
Spacing and layout guidelines (margins, paddings, and alignment)
Ensure the design remains clean, modern, and professional while maintaining usability and accessibility.
Provide design mockups or visual examples (if possible) to illustrate the proposed changes.
Deliverables:
A UI Style Guide (PDF or Figma file) with specifications on fonts, colors, spacing, and UI components.
Optionally, before/after mockups or examples demonstrating the improvements.
Ideal Designer:
Strong experience in mobile UI/UX design.
Understanding of modern design trends and best practices.
Ability to communicate design choices clearly for easy developer implementation.
I have attached 7 images showcasing the main UI screens used in the FlorvaLink app. These screens need visual enhancements to improve their overall look and user experience.
The images represent the current design in three key modes:
LIST Mode – Displays data in a structured list format.
READ Mode – Shows detailed information when a user selects an item.
ADD/EDIT Mode – Allows users to input or modify information.
Additionally, there is a ‘MORE’ page, which serves as a menu listing other features of the application.
Task Objective:
Please refine and improve these UIs to create a more modern, visually appealing, and user-friendly experience. Focus on typography, colors, spacing, and component styling to ensure a cohesive and polished design.
Look and feel
Each slider illustrates characteristics of the customer's brand and the style your logo design should communicate.

```html
<!DOCTYPE html>
<html lang="en">
<head>
<meta charset="utf-8">
<title>FlorvaLink app – App Style Guideline</title>
<link href="https://fonts.googleapis.com/css2?family=Inter:wght@400;500;600;700;800&display=swap" rel="stylesheet">
<style>
:root{
  --blue:#0050A3;
  --blue-pale:#ECF1F7;
  --sky:#CCEEFA;
  --ink:#424242;
  --grey:#BCBCBC;
  --cyan:#B2E2FF;
  --mint:#AFFEAF;
  --cream:#FFFDBD;
  --stroke:#EDEDED;
  --label:#B5B5B5;
  --line:#E9EEF4;
  --error:#E5484D;
  --white:#FFFFFF;
}
*{margin:0;padding:0;box-sizing:border-box}
html,body{width:1200px;height:5098px;overflow:hidden;background:var(--white)}
body{font-family:'Inter',sans-serif;color:var(--ink);position:relative}
.abs{position:absolute}
.guide-rail{position:absolute;left:1046px;top:800px;width:1px;height:4298px;background:var(--line)}
.hero{position:absolute;left:0;top:0;width:1200px;height:800px;
  background:linear-gradient(180deg,#3e5f9e 0%,#6f86bb 30%,#c79aa9 52%,#e9b59a 66%,#f2c98f 74%,#4a4f3a 82%,#2b3423 100%)}
.hero-name{left:93px;top:66px;font-size:36px;font-weight:600;color:var(--white)}
.hero-kicker{left:93px;top:528px;font-size:74px;font-weight:400;color:var(--white);letter-spacing:1px}
.hero-title{left:90px;top:622px;font-size:106px;font-weight:800;color:var(--white);letter-spacing:1px}
.band{position:absolute;left:0;width:1200px;height:83px;border-top:1px solid var(--line);border-bottom:1px solid var(--line)}
.badge{position:absolute;left:1046px;width:83px;height:83px;background:var(--blue);color:var(--white);font-size:32px;font-weight:600;display:flex;align-items:center;justify-content:center}
.section-title{position:absolute;left:92px;font-size:36px;font-weight:700;color:var(--blue)}
.label{position:absolute;font-size:23px;color:var(--label);font-weight:400}
.swatch{position:absolute;border:2px solid var(--stroke);border-radius:8px;overflow:hidden;display:flex;flex-direction:column}
.swatch .fill{flex:1}
.swatch .code{height:30px;background:var(--white);font-size:12px;font-weight:700;color:var(--ink);display:flex;align-items:center;justify-content:center}
.swatch.primary{width:139px;height:192px;top:1040px}
.swatch.secondary{width:121px;height:167px;top:1378px}
.swatch.secondary .code{border:2px solid var(--ink);border-radius:0 0 8px 8px;height:26px}
.swatch.main{border-color:var(--blue)}
.font-name{left:93px;top:1826px;font-size:32px;font-weight:500;color:var(--blue)}
.pill{position:absolute;top:1830px;height:33px;border-radius:17px;background:var(--blue);color:var(--white);font-size:16px;display:flex;align-items:center;justify-content:center}
.alphabet{left:93px;font-size:23px;font-weight:500;color:var(--ink);word-spacing:6px;letter-spacing:4px}
.type-table{left:91px;top:2014px;width:861px;height:95px;border:2px solid var(--stroke);display:flex}
.type-table .cell{flex:1;border-right:2px solid var(--stroke);display:flex;flex-direction:column;align-items:center;justify-content:center;gap:10px}
.type-table .cell:last-child{border-right:none}
.type-table .cap{font-size:19px;color:var(--label)}
.type-table .val{font-size:20px;color:var(--ink)}
.icon{position:absolute;width:46px;height:46px}
.body-text{left:95px;font-size:19px;line-height:32px;color:var(--ink)}
.link{text-decoration:underline}
.field{position:absolute;width:366px;height:56px;border:2px solid var(--stroke);border-radius:8px;background:var(--white)}
.field .ico{position:absolute;left:16px;top:14px;width:24px;height:24px}
.field .hint{position:absolute;left:58px;top:10px;font-size:10px;color:var(--label)}
.field .value{position:absolute;left:58px;top:28px;font-size:13px;color:var(--ink)}
.field.error{border-color:var(--error)}
.note{position:absolute;font-size:12px;font-weight:600;color:var(--ink);line-height:15px}
.dropdown-list{position:absolute;left:592px;top:3132px;width:364px;height:141px;border:2px solid var(--stroke);border-top:none;border-radius:0 0 8px 8px}
.dropdown-list div{position:absolute;left:22px;font-size:12px;color:var(--ink)}
.btn{position:absolute;top:3621px;height:30px;border-radius:15px;background:var(--blue);color:var(--white);font-size:11px;font-weight:600;display:flex;align-items:center;justify-content:center;gap:6px}
.spec{position:absolute;font-size:10px;font-weight:700;color:var(--ink)}
.social-card{position:absolute;left:647px;top:3610px;width:149px;height:120px;border:2px solid var(--stroke);border-radius:14px;display:flex;flex-direction:column;align-items:center;justify-content:center;gap:8px;font-size:11px;text-align:center;color:var(--ink)}
.chip{position:absolute;top:3750px;height:20px;font-size:10px;color:var(--ink);display:flex;align-items:center}
.chip.active{background:var(--blue);color:var(--white);border-radius:10px;padding:0 8px}
.phone{position:absolute;left:99px;top:4073px;width:348px;height:946px;border:3px solid #d9dde4;border-radius:22px;overflow:hidden;background:var(--white)}
.phone-head{position:absolute;left:0;top:0;width:100%;height:110px;background:linear-gradient(180deg,#1f4f92,#3d6db0)}
.tile{position:absolute;width:152px;height:128px;border-radius:18px;background:#f7e3ea;display:flex;flex-direction:column;align-items:center;justify-content:center;gap:10px;font-size:11px;color:var(--ink);text-align:center;line-height:14px}
.group{position:absolute;left:16px;width:316px;border-radius:10px;padding:14px 10px}
.group .g-title{font-size:11px;font-weight:600;color:var(--ink)}
.group .g-field{margin-top:10px;background:var(--white);border-radius:8px;padding:9px 10px;font-size:10px;line-height:16px;color:var(--ink);position:relative}
.group .g-btn{display:inline-block;margin-top:10px;background:var(--blue);color:var(--white);font-size:10px;border-radius:10px;padding:4px 14px}
.column{position:absolute;top:0;width:73px;height:100%;background:rgba(240,150,175,.18)}
.navbar{position:absolute;left:0;bottom:0;width:100%;height:68px;background:var(--white);border-top:1px solid var(--stroke)}
.callout{position:absolute;font-size:16px;font-weight:600;color:var(--ink)}
.rule{position:absolute;height:1px;background:var(--ink)}
</style>
</head>
<body>
<div class="guide-rail"></div>

<div class="hero" role="img" aria-label="Passenger airliner taking off low over a grass field against a sunset sky"></div>
<div class="abs hero-name">FlorvaLink app</div>
<div class="badge" style="top:48px">01</div>
<div class="abs hero-kicker">APP STYLE</div>
<div class="abs hero-title">GUIDELINE</div>

<div class="band" style="top:848px"></div>
<div class="section-title" style="top:866px">Color Palette</div>
<div class="badge" style="top:848px">02</div>
<div class="label" style="left:92px;top:980px">Primary Colors (for background , icon , icon bg)</div>
<div class="swatch primary main" style="left:95px"><div class="fill" style="background:var(--blue)"></div><div class="code">#0050A3</div></div>
<div class="swatch primary" style="left:273px"><div class="fill" style="background:var(--blue-pale)"></div><div class="code">#ECF1F7</div></div>
<div class="swatch primary" style="left:446px"><div class="fill" style="background:var(--sky)"></div><div class="code">#CCEEFA</div></div>

<div class="label" style="left:92px;top:1307px">Secondary Colors (for text , icon, bg)</div>
<div class="label" style="left:826px;top:1307px;line-height:28px">Form text-field<br>stroke(border)</div>
<div class="swatch secondary" style="left:93px"><div class="fill" style="background:var(--ink)"></div><div class="code">#424242</div></div>
<div class="swatch secondary" style="left:234px"><div class="fill" style="background:var(--grey)"></div><div class="code">#BCBCBC</div></div>
<div class="swatch secondary" style="left:374px"><div class="fill" style="background:var(--cyan)"></div><div class="code">#B2E2FF</div></div>
<div class="swatch secondary" style="left:515px"><div class="fill" style="background:var(--mint)"></div><div class="code">#AFFEAF</div></div>
<div class="swatch secondary" style="left:660px"><div class="fill" style="background:var(--cream)"></div><div class="code">#FFFDBD</div></div>
<div class="swatch secondary" style="left:832px;border-color:var(--stroke)"><div class="fill" style="background:var(--stroke)"></div><div class="code" style="border:none">#EDEDED</div></div>

<div class="band" style="top:1649px"></div>
<div class="section-title" style="top:1669px">Typography</div>
<div class="badge" style="top:1649px">03</div>
<div class="label" style="left:92px;top:1782px">Font Used</div>
<div class="abs font-name">Inter</div>
<div class="pill" style="left:244px;width:140px;font-weight:500">Medium</div>
<div class="pill" style="left:406px;width:184px;font-weight:600">Semi-bold</div>
<div class="pill" style="left:624px;width:184px;font-weight:700">Bold</div>
<div class="abs alphabet" style="top:1900px">a b c d e f g h i j k l m n o p q r s t u v w x y z</div>
<div class="abs alphabet" style="top:1947px">A B C D E F G H I J K L M N O P Q R S T U V W X Y Z</div>
<div class="abs type-table">
  <div class="cell"><span class="cap">Heading - Bold</span><span class="val" style="font-weight:700">Work Order 22px</span></div>
  <div class="cell"><span class="cap">Small Title - Semi-bold</span><span class="val" style="font-weight:600">Address Information, 18px</span></div>
  <div class="cell"><span class="cap">Other Text - Medium</span><span class="val" style="font-weight:500">Full name 16px</span></div>
</div>

<div class="band" style="top:2224px"></div>
<div class="section-title" style="top:2243px">Icons</div>
<div class="badge" style="top:2224px">04</div>
<div class="label" style="left:90px;top:2345px">Line icons</div>
<svg class="icon" style="left:90px;top:2397px" viewBox="0 0 24 24" fill="none" stroke="#BCBCBC" stroke-width="1.4"><rect x="2" y="7" width="20" height="14" rx="2"/><path d="M9 7V5h6v2M2 12h20M11 12v2h2v-2"/></svg>
<svg class="icon" style="left:166px;top:2397px" viewBox="0 0 24 24" fill="none" stroke="#BCBCBC" stroke-width="1.4"><circle cx="12" cy="8" r="4"/><path d="M4 21c0-4 3.6-7 8-7s8 3 8 7z"/></svg>
<svg class="icon" style="left:232px;top:2397px" viewBox="0 0 24 24" fill="none" stroke="#BCBCBC" stroke-width="1.4"><path d="M12 22s7-7 7-12a7 7 0 0 0-14 0c0 5 7 12 7 12z"/><circle cx="12" cy="10" r="2.5"/></svg>
<svg class="icon" style="left:308px;top:2397px" viewBox="0 0 24 24" fill="none" stroke="#BCBCBC" stroke-width="1.4"><rect x="3" y="3" width="11" height="18"/><path d="M14 9h6v12h-6M6 7h2M9 7h2M6 11h2M9 11h2M6 15h2M9 15h2"/></svg>
<svg class="icon" style="left:380px;top:2400px;width:38px;height:38px" viewBox="0 0 24 24" fill="none" stroke="#BCBCBC" stroke-width="1.6"><path d="M6 9l6 6 6-6"/></svg>
<svg class="icon" style="left:454px;top:2397px" viewBox="0 0 24 24" fill="none" stroke="var(--blue)" stroke-width="1.4"><path d="M3 13c0-4 4-7 9-7s9 3 9 7"/><path d="M2 13h20v3H2zM8 9h8"/></svg>
<svg class="icon" style="left:531px;top:2397px" viewBox="0 0 24 24" fill="none" stroke="var(--blue)" stroke-width="1.4"><rect x="4" y="2" width="16" height="18" rx="2"/><path d="M8 7h8M8 11h5"/><circle cx="14" cy="16" r="3"/><path d="M13 19l-1 4 2-1 2 1-1-4"/></svg>
<svg class="icon" style="left:599px;top:2397px" viewBox="0 0 24 24" fill="none" stroke="var(--blue)" stroke-width="1.4"><path d="M12 2l8 3v6c0 5-3.5 9-8 11-4.5-2-8-6-8-11V5z"/><path d="M12 8v7M8.5 11.5h7"/></svg>
<svg class="icon" style="left:670px;top:2397px" viewBox="0 0 24 24" fill="none" stroke="var(--blue)" stroke-width="1.4"><path d="M3 5h13v11H8l-5 4z"/><path d="M6 9h7M6 12h5"/><path d="M19 2l1 2 2 .5-1.5 1.5.4 2-1.9-1-1.9 1 .4-2L16 4.5 18 4z"/></svg>

<div class="label" style="left:90px;top:2502px">Bold icons</div>
<svg class="icon" style="left:86px;top:2551px" viewBox="0 0 24 24" fill="var(--blue)"><rect x="4" y="2" width="16" height="20" rx="4"/><rect x="2" y="6" width="3" height="3" rx="1"/><rect x="2" y="14" width="3" height="3" rx="1"/><circle cx="12" cy="10" r="3" fill="#fff"/><path d="M7 18c0-3 2.2-4.5 5-4.5s5 1.5 5 4.5z" fill="#fff"/></svg>
<svg class="icon" style="left:161px;top:2551px" viewBox="0 0 24 24" fill="var(--blue)"><path d="M12 2a10 10 0 0 1 10 10c0 5.5-4.5 10-10 10H3l2-3A10 10 0 0 1 12 2z"/><path d="M8 9h3v3l-2 3M13 9h3v3l-2 3" stroke="#fff" stroke-width="1.4" fill="none"/></svg>
<svg class="icon" style="left:234px;top:2551px" viewBox="0 0 24 24" fill="var(--blue)"><path d="M9 5V3h6v2" stroke="var(--blue)" stroke-width="2" fill="none"/><rect x="2" y="6" width="20" height="15" rx="3"/><path d="M2 12h20" stroke="#fff" stroke-width="1.5"/><rect x="10.5" y="10.5" width="3" height="3" fill="#fff"/></svg>
<svg class="icon" style="left:310px;top:2551px" viewBox="0 0 24 24" fill="var(--blue)"><rect x="3" y="3" width="18" height="19" rx="3"/><rect x="7" y="1" width="2" height="4"/><rect x="15" y="1" width="2" height="4"/><path d="M7 10h10M7 14h10M7 18h6" stroke="#fff" stroke-width="1.6"/></svg>
<svg class="icon" style="left:385px;top:2551px" viewBox="0 0 24 24" fill="var(--blue)"><rect x="2" y="2" width="9" height="9" rx="3"/><rect x="13" y="2" width="9" height="9" rx="3"/><rect x="2" y="13" width="9" height="9" rx="3"/><rect x="13" y="13" width="9" height="9" rx="3"/></svg>

<div class="abs body-text" style="top:2638px">All icons taken from <span class="link">www.iconharbor.com</span></div>
<div class="abs body-text" style="top:2684px;width:910px">For icons, I've used a range of 24px to 30px, as the varying icon shapes require flexible sizing. However, to ensure consistency, we could consider adopting Orbit Icons, which come in a standardized size, simplifying our design and maintaining visual harmony</div>

<div class="band" style="top:2891px"></div>
<div class="section-title" style="top:2910px">Form Fields</div>
<div class="badge" style="top:2891px">05</div>

<div class="label" style="left:91px;top:3014px">Default State</div>
<div class="note" style="left:255px;top:3041px">Top Padding 16px</div>
<div class="note" style="left:47px;top:3077px">Left<br>20px</div>
<div class="note" style="left:466px;top:3077px">Right<br>20px</div>
<div class="field" style="left:91px;top:3059px">
  <div class="abs" style="left:0;top:0;width:100%;height:12px;background:rgba(240,150,175,.35)"></div>
  <div class="abs" style="left:0;bottom:0;width:100%;height:12px;background:rgba(240,150,175,.35)"></div>
  <div class="abs" style="left:0;top:0;width:20px;height:100%;background:rgba(180,150,240,.35)"></div>
  <div class="abs" style="right:0;top:0;width:20px;height:100%;background:rgba(180,150,240,.35)"></div>
  <svg class="ico" viewBox="0 0 24 24" fill="none" stroke="#BCBCBC" stroke-width="1.5"><rect x="2" y="7" width="20" height="14" rx="2"/><path d="M9 7V5h6v2M2 12h20"/></svg>
  <div class="hint" style="top:14px">Business Name -e</div>
</div>
<div class="note" style="left:129px;top:3124px">20px</div>
<div class="note" style="left:255px;top:3124px">Bottom Padding 16px</div>

<div class="label" style="left:91px;top:3163px">Active State</div>
<div class="field" style="left:91px;top:3204px;height:53px">
  <svg class="ico" viewBox="0 0 24 24" fill="none" stroke="#BCBCBC" stroke-width="1.5"><rect x="2" y="7" width="20" height="14" rx="2"/><path d="M9 7V5h6v2M2 12h20"/></svg>
  <div class="hint">Business Name -e</div><div class="value">Contact Business name</div>
</div>

<div class="label" style="left:91px;top:3288px">Error State</div>
<div class="field error" style="left:91px;top:3335px;height:53px">
  <svg class="ico" viewBox="0 0 24 24" fill="none" stroke="var(--error)" stroke-width="1.5"><rect x="2" y="7" width="20" height="14" rx="2"/><path d="M9 7V5h6v2M2 12h20"/></svg>
  <div class="hint">Business Name -e</div><div class="value">Contact Busines</div>
</div>

<div class="label" style="left:592px;top:3020px">Dropdown</div>
<div class="field" style="left:592px;top:3075px;width:364px;height:57px;border-radius:8px 8px 0 0">
  <svg class="ico" viewBox="0 0 24 24" fill="none" stroke="#BCBCBC" stroke-width="1.5"><rect x="2" y="7" width="20" height="14" rx="2"/><path d="M9 7V5h6v2M2 12h20"/></svg>
  <div class="hint">Address Label Tag -e</div><div class="value">Address label tag one</div>
  <svg class="abs" style="right:18px;top:20px;width:14px;height:14px" viewBox="0 0 24 24" fill="none" stroke="var(--blue)" stroke-width="2.5"><path d="M6 9l6 6 6-6"/></svg>
</div>
<div class="dropdown-list">
  <div style="top:16px">Address label tag one</div>
  <div style="top:50px">Address label tag two</div>
  <div style="top:82px">Address label tag three</div>
  <div style="top:111px">Address label tag four</div>
</div>
<div class="field" style="left:592px;top:3307px;width:303px;height:43px">
  <div class="value" style="left:16px;top:12px;font-size:12px">Search</div>
  <svg class="abs" style="right:10px;top:14px;width:13px;height:13px" viewBox="0 0 24 24" fill="none" stroke="#BCBCBC" stroke-width="2"><circle cx="10" cy="10" r="7"/><path d="M15 15l6 6"/></svg>
</div>

<div class="band" style="top:3461px"></div>
<div class="section-title" style="top:3481px">Buttons</div>
<div class="badge" style="top:3461px">06</div>
<div class="label" style="left:91px;top:3586px;font-size:20px">Buttons</div>
<div class="btn" style="left:91px;width:59px">Save</div>
<div class="btn" style="left:170px;width:101px"><svg width="14" height="14" viewBox="0 0 24 24" fill="#fff"><rect x="4" y="2" width="16" height="20" rx="4"/><circle cx="12" cy="10" r="3" fill="var(--blue)"/><path d="M7 18c0-3 2.2-4.5 5-4.5s5 1.5 5 4.5z" fill="var(--blue)"/></svg>Contact</div>
<div class="btn" style="left:293px;width:139px">Add Aircraft Owner</div>
<div class="spec" style="left:91px;top:3671px">spacing&nbsp; Padding Left &amp;&nbsp; right 20px and&nbsp; up &amp; down 10px</div>

<div class="social-card">
  <svg width="30" height="30" viewBox="0 0 24 24" fill="none" stroke="var(--blue)" stroke-width="1.5"><rect x="2" y="7" width="20" height="14" rx="2"/><path d="M9 7V5h6v2M2 12h20M11 12v2h2v-2"/></svg>
  <span>Add Social<br>Media -e</span>
</div>
<div class="spec" style="left:659px;top:3757px">spacing&nbsp; Padding Left &amp;&nbsp; right 10px and&nbsp; up &amp; down 20px</div>

<div class="label" style="left:91px;top:3708px;font-size:20px">Chip Menu</div>
<div class="chip active" style="left:91px">All</div>
<div class="chip" style="left:135px">Aircraft Owner</div>
<div class="chip" style="left:236px">Enthusiast -e</div>
<div class="chip" style="left:331px">Pilot</div>
<div class="chip" style="left:378px;color:#1f9a3a;font-weight:600">Aircraft Owner</div>
<div class="spec" style="left:91px;top:3792px">spacing&nbsp; Padding Left &amp;&nbsp; right 10px and&nbsp; up &amp; down 5px</div>

<div class="band" style="top:3922px"></div>
<div class="section-title" style="top:3942px">Layout Spacing</div>
<div class="badge" style="top:3922px">07</div>

<div class="phone">
  <div class="phone-head" role="img" aria-label="Faint aircraft photo behind the screen header"></div>
  <div class="abs" style="left:14px;top:20px;font-size:10px;color:#fff">12:30PM</div>
  <div class="abs" style="left:0;top:54px;width:100%;text-align:center;font-size:15px;font-weight:700;color:#fff">Contact</div>
  <div class="abs" style="left:14px;top:54px;width:18px;height:18px;border-radius:50%;background:rgba(255,255,255,.3)"></div>
  <div class="abs" style="right:14px;top:54px;width:18px;height:18px;border-radius:50%;background:rgba(255,255,255,.3)"></div>

  <div class="tile" style="left:16px;top:109px"><svg width="26" height="26" viewBox="0 0 24 24" fill="none" stroke="var(--blue)" stroke-width="1.4"><circle cx="12" cy="8" r="4"/><path d="M4 21c0-4 3.6-7 8-7s8 3 8 7z"/></svg>Add Personal<br>Information -e</div>
  <div class="tile" style="left:184px;top:109px"><svg width="26" height="26" viewBox="0 0 24 24" fill="none" stroke="var(--blue)" stroke-width="1.4"><rect x="2" y="7" width="20" height="14" rx="2"/><path d="M9 7V5h6v2M2 12h20"/></svg>Add Work<br>Info -e</div>
  <div class="tile" style="left:16px;top:249px;background:#f3eef0"><svg width="26" height="26" viewBox="0 0 24 24" fill="none" stroke="var(--blue)" stroke-width="1.4"><circle cx="12" cy="12" r="4"/><circle cx="12" cy="12" r="8" stroke-dasharray="3 2"/></svg>Add Skills /<br>Talents -e</div>
  <div class="tile" style="left:184px;top:249px;background:#f3eef0"><svg width="26" height="26" viewBox="0 0 24 24" fill="none" stroke="var(--blue)" stroke-width="1.4"><rect x="4" y="3" width="16" height="18" rx="2"/><path d="M10 9a2 2 0 1 1 2 2v2M12 16v1"/></svg>Add<br>Resources -e</div>

  <div class="group" style="top:396px;height:95px;background:#fff0bf">
    <div class="g-title">Pilots -e</div>
    <div class="g-field">Halvorsen, Dara, 5120833, 10/31/23</div>
  </div>
  <div class="group" style="top:505px;height:148px;background:#d6dfee">
    <div class="g-title">Aircraft Owner -e</div>
    <div class="g-field">Halvorsen, Dara; Brellix: Q7: Brellix<br>Aircraft Company, Single Engine, 1100</div>
    <div class="g-btn">Add Aircraft Owner</div>
  </div>
  <div class="group" style="top:675px;height:143px;background:#d4f3c9">
    <div class="g-title">Qualified Pilot -e</div>
    <div class="g-field">Halvorsen, Dara; Brellix: Q7: Brellix<br>Aircraft Company, Single Engine, 1100</div>
    <div class="g-btn">Add Qualified Pilot -e</div>
  </div>

  <div class="column" style="left:16px"></div>
  <div class="column" style="left:97px"></div>
  <div class="column" style="left:178px"></div>
  <div class="column" style="left:259px"></div>

  <div class="navbar">
    <div class="abs" style="left:22px;top:15px;width:95px;height:32px;border-radius:16px;background:var(--blue);color:#fff;font-size:11px;display:flex;align-items:center;justify-content:center;gap:6px">Contact</div>
    <div class="abs" style="left:148px;top:22px;width:18px;height:18px;border-radius:50%;border:2px solid var(--cyan)"></div>
    <div class="abs" style="left:198px;top:22px;width:18px;height:16px;border-radius:3px;border:2px solid var(--cyan)"></div>
    <div class="abs" style="left:250px;top:22px;width:16px;height:18px;border-radius:3px;border:2px solid var(--cyan)"></div>
    <div class="abs" style="left:300px;top:22px;width:18px;height:18px;border-radius:3px;border:2px dotted var(--cyan)"></div>
  </div>
</div>
<div class="rule" style="left:234px;top:5022px;width:1px;height:18px"></div>
<div class="note" style="left:222px;top:5040px;font-size:11px">35px</div>

<div class="abs" style="left:487px;top:4094px;width:520px;font-size:16px;line-height:27px;color:var(--ink)">I've based the design on a 4-column grid system, using the Nova Phone Max (440px x 956px) as the reference device. To ensure a clean and uncluttered layout, I've applied a 20px margin (adjustable to 16px if needed) to the left and right sides, and maintained a consistent 16px spacing between objects. This approach provides a clear, visually appealing design that optimizes the screen real estate</div>
<div class="rule" style="left:358px;top:4313px;width:160px"></div>
<div class="callout" style="left:527px;top:4302px">spacing between objects :16 px.</div>
<div class="rule" style="left:440px;top:4398px;width:72px"></div>
<div class="callout" style="left:519px;top:4387px">Layout Margin left &amp; right:20 px.</div>
</body>
</html>
```